Business Card Design needed for logo design project

This project is linked to Verdane acupuncture - Sabine LEROUX.

Our company needs a Business Card Design. Please refer to our original project in the link above.

Industry/Entity Type

Business

```html
<!DOCTYPE html>
<html lang="en">
<head>
<meta charset="utf-8">
<title>Verdane acupuncture – Business Card</title>
<link rel="stylesheet" href="https://fonts.googleapis.com/css2?family=Arvo:wght@700&family=Share+Tech&family=Share+Tech+Mono&family=Oranienbaum&display=swap">
<style>
  :root {
    --slate: #455258;
    --panel: #dde3e4;
    --sky: #3cc4e0;
    --aqua: #52e0e3;
    --bar: #5ae8e8;
    --jade: #3fc6a6;
    --ink: #111417;
    --name: #2b7c72;
    --white: #ffffff;
    --badge: #2f7fe6;
  }
  html, body {
    margin: 0;
    padding: 0;
    width: 1200px;
    height: 685px;
    overflow: hidden;
    background: var(--slate);
  }
  .card {
    display: block;
    width: 1200px;
    height: 685px;
  }
  .bg-slate { fill: var(--slate); }
  .bg-panel { fill: var(--panel); }
  .strip-sky { fill: var(--sky); }
  .column-aqua { fill: var(--aqua); }
  .fold-jade { fill: var(--jade); }
  .contact-bar { fill: var(--bar); }
  .icon-ring { fill: var(--aqua); stroke: var(--white); stroke-width: 3.5; filter: drop-shadow(0 2px 2px rgba(0,0,0,.35)); }
  .icon-glyph { fill: var(--white); }
  .icon-line { fill: none; stroke: var(--white); stroke-width: 1.6; }
  .label-name { font-family: "Arvo", serif; font-weight: 700; font-size: 19px; fill: var(--ink); letter-spacing: 1px; }
  .label-designation { font-family: "Arvo", serif; font-weight: 700; font-size: 14px; fill: var(--ink); letter-spacing: 1px; }
  .brand-dot { fill: var(--badge); stroke: #1b2a33; stroke-width: 4; }
  .brand-name { font-family: "Arvo", serif; font-weight: 700; font-size: 13px; fill: var(--ink); }
  .person-name { font-family: "Share Tech", sans-serif; font-size: 29px; fill: var(--name); filter: drop-shadow(1px 1px 1px rgba(0,0,0,.5)); }
  .tagline { font-family: "Arvo", serif; font-weight: 700; font-size: 20px; fill: var(--ink); letter-spacing: 1px; }
  .contact-phone { font-family: "Share Tech Mono", monospace; font-size: 22px; fill: var(--white); letter-spacing: 4px; filter: drop-shadow(2px 2px 1px rgba(0,0,0,.45)); }
  .contact-text { font-family: "Oranienbaum", serif; font-size: 25px; fill: var(--white); filter: drop-shadow(2px 2px 1px rgba(0,0,0,.45)); }
</style>
</head>
<body>
<svg class="card" viewBox="0 0 788 450" preserveAspectRatio="none" xmlns="http://www.w3.org/2000/svg">
  <rect class="bg-slate" x="0" y="0" width="788" height="450"/>
  <rect class="bg-panel" x="0" y="50" width="788" height="350"/>
  <rect class="strip-sky" x="0" y="50" width="50" height="350"/>

  <polygon class="fold-jade" points="350,28 383,50 350,50"/>
  <polygon class="fold-jade" points="350,400 383,400 350,420"/>
  <rect class="column-aqua" x="250" y="28" width="100" height="392"/>

  <g class="contact-rows">
    <g transform="translate(0,0)">
      <polygon class="fold-jade" points="350,80 374,94 374,132 350,146"/>
      <rect class="contact-bar" x="374" y="94" width="391" height="38"/>
      <polygon class="fold-jade" points="765,94 788,80 788,146 765,132"/>
    </g>
    <g transform="translate(0,81)">
      <polygon class="fold-jade" points="350,80 374,94 374,132 350,146"/>
      <rect class="contact-bar" x="374" y="94" width="391" height="38"/>
      <polygon class="fold-jade" points="765,94 788,80 788,146 765,132"/>
    </g>
    <g transform="translate(0,161)">
      <polygon class="fold-jade" points="350,80 374,94 374,132 350,146"/>
      <rect class="contact-bar" x="374" y="94" width="391" height="38"/>
      <polygon class="fold-jade" points="765,94 788,80 788,146 765,132"/>
    </g>
    <g transform="translate(0,241)">
      <polygon class="fold-jade" points="350,80 374,94 374,132 350,146"/>
      <rect class="contact-bar" x="374" y="94" width="391" height="38"/>
      <polygon class="fold-jade" points="765,94 788,80 788,146 765,132"/>
    </g>
  </g>

  <g class="icon phone">
    <circle class="icon-ring" cx="301" cy="112" r="25"/>
    <path class="icon-glyph" d="M290 108 q11 -8 22 0 l-2 4 h-4 l-1 -3 q-4 -1 -8 0 l-1 3 h-4 z M292 113 h16 l2 9 h-20 z"/>
    <circle cx="301" cy="117" r="2.5" fill="var(--aqua)"/>
  </g>
  <g class="icon email">
    <circle class="icon-ring" cx="301" cy="192" r="25"/>
    <text x="301" y="203" text-anchor="middle" font-family="Arial, sans-serif" font-size="30" font-weight="700" class="icon-glyph">@</text>
  </g>
  <g class="icon web">
    <circle class="icon-ring" cx="301" cy="272" r="25"/>
    <circle class="icon-line" cx="301" cy="272" r="13"/>
    <ellipse class="icon-line" cx="301" cy="272" rx="6" ry="13"/>
    <line class="icon-line" x1="288" y1="272" x2="314" y2="272"/>
    <line class="icon-line" x1="301" y1="259" x2="301" y2="285"/>
    <line class="icon-line" x1="290" y1="265" x2="312" y2="265"/>
    <line class="icon-line" x1="290" y1="279" x2="312" y2="279"/>
  </g>
  <g class="icon location">
    <circle class="icon-ring" cx="301" cy="352" r="25"/>
    <path class="icon-glyph" d="M301 370 L292 352 A10.5 10.5 0 1 1 310 352 Z"/>
    <circle cx="301" cy="345" r="4" fill="var(--aqua)"/>
  </g>

  <text class="contact-phone" x="404" y="122">763-555-0187</text>
  <text class="contact-text" x="406" y="203">info@verdanemail.com</text>
  <text class="contact-text" x="406" y="282">www.verdanecare.com</text>
  <text class="contact-text" x="408" y="363">address here</text>

  <text class="label-name" x="60" y="92">Name</text>
  <text class="label-designation" x="60" y="117">Designation</text>

  <g class="brand-mark">
    <circle class="brand-dot" cx="150" cy="198" r="38"/>
    <text class="brand-name" x="150" y="262" text-anchor="middle">Verdane acupuncture</text>
  </g>

  <text class="person-name" x="55" y="327" textLength="188" lengthAdjust="spacingAndGlyphs">Sabine LEROUX</text>
  <text class="tagline" x="148" y="364" text-anchor="middle">Get balanced</text>
  <text class="tagline" x="151" y="390" text-anchor="middle">and be healthy</text>
</svg>
</body>
</html>
```